Vantel Solutions Website Design

We are a B2B startup offering a free virtual data room and deal management platform for small businesses. We need a 10-page website geared towards business executives and entrepreneurs that is simple, uploads quickly and provides a good introduction to our product. We've attached a document setting forth the text of 8 of the 10 pages (the other two - Resources and Blog - need to be designed to allow the future posting of white papers and blog entries) and links to the screenshots and GIFs, all of which are in a folder on filewell. We've also attached a zip file with our logo and a pdf file with our font and colors. Examples of websites we like include www.marbletoft.example, www.usepivra.example and https://kelmo.example.

Target Market(s)

Small business owners, business executives and entrepreneurs

Industry/Entity Type

Finance

Coding

Number of Pages Required

5+ page

Font styles to use
Sans Serif

Colors
85abd2
f9ba93

Requirements
Must have
• Please use the Wordpress harbor theme I uploaded to code the site.
Nice to have
• Clean, uncluttered design. White background. Screenshots and gifs should be shown on monitors (desktop, laptop and iPad only). Blue and orange are our corporate colors, but you’re not limited to those two colors. See uploaded logo guide for complementary colors or use your own judgment.

```html
<!DOCTYPE html>
<html lang="en">
<head>
<meta charset="UTF-8">
<title>Vantel – Manage Your Workflow Better</title>
<link rel="stylesheet" href="https://fonts.googleapis.com/css2?family=Barlow:wght@300;400;500;600;700&display=swap">
<style>
  :root {
    --brand-blue: #85abd2;
    --brand-orange: #f9ba93;
    --logo-slate: #4f7388;
    --ink: #2f3541;
    --ink-soft: #5f636b;
    --nav-ink: #2b2f38;
    --bullet-red: #ec5a5a;
    --page-bg: #f6f6fb;
    --header-bg: #ffffff;
    --device-frame: #111214;
    --app-bar: #4a7189;
    --app-body: #eef0f2;
  }
  * { box-sizing: border-box; margin: 0; padding: 0; }
  html, body {
    width: 1200px; height: 565px; overflow: hidden;
    font-family: "Barlow", Arial, sans-serif;
    background: var(--page-bg);
  }
  body { position: relative; }
  .site-header {
    position: absolute; top: 0; left: 0; width: 1200px; height: 71px;
    background: var(--header-bg);
  }
  .brand {
    position: absolute; left: 90px; top: 10px;
    font-size: 44px; font-weight: 600; color: var(--logo-slate);
    letter-spacing: -0.5px; line-height: 50px;
  }
  .main-nav a {
    position: absolute; top: 28px;
    font-size: 14px; font-weight: 500; letter-spacing: 1.3px;
    text-transform: uppercase; color: var(--nav-ink); text-decoration: none;
    line-height: 16px;
  }
  .main-nav a.is-active {
    color: var(--brand-orange);
    border-bottom: 1px solid var(--brand-orange);
  }
  .nav-home { left: 486px; }
  .nav-features { left: 564px; }
  .nav-clients { left: 676px; }
  .nav-company { left: 807px; }
  .nav-contact { left: 913px; }
  .cta-button {
    position: absolute; left: 1012px; top: 18px; width: 98px; height: 35px;
    background: var(--brand-orange); color: #fff;
    font-size: 14px; font-weight: 600; text-align: center; line-height: 35px;
    text-decoration: none;
    box-shadow: 0 6px 14px rgba(249, 186, 147, 0.45);
  }
  .hero {
    position: absolute; top: 71px; left: 0; width: 1200px; height: 494px;
    overflow: hidden;
  }
  .hero-title {
    position: absolute; top: 54px; width: 100%; text-align: center;
    font-size: 45px; font-weight: 300; color: var(--ink); letter-spacing: 0.5px;
    line-height: 56px;
  }
  .hero-intro {
    position: absolute; top: 110px; width: 100%; text-align: center;
    font-size: 18px; font-weight: 400; color: var(--ink); line-height: 27px;
  }
  .hero-intro strong { color: var(--brand-blue); font-weight: 600; }
  .feature-list { list-style: none; }
  .feature-list li {
    position: absolute; top: 172px;
    font-size: 15.5px; color: var(--ink-soft); line-height: 20px;
    padding-left: 30px; white-space: nowrap;
  }
  .feature-list li::before {
    content: ""; position: absolute; left: 0; top: 5px;
    width: 10px; height: 10px; border-radius: 50%; background: var(--bullet-red);
  }
  .feature-collab { left: 126px; }
  .feature-custom { left: 474px; }
  .feature-free { left: 759px; }
  .device {
    position: absolute; left: 182px; top: 247px; width: 836px; height: 247px;
    background: var(--device-frame); border-radius: 26px 26px 0 0;
    box-shadow: 0 0 0 2px #2c2d30 inset;
    overflow: hidden;
  }
  .device-screen {
    position: absolute; left: 38px; top: 38px; width: 756px; height: 209px;
    background: linear-gradient(180deg, var(--app-bar) 0, var(--app-bar) 32px, var(--app-body) 32px, #f7f8f9 100%);
  }
</style>
</head>
<body>
  <header class="site-header">
    <div class="brand">Vantel</div>
    <nav class="main-nav">
      <a class="nav-home is-active" href="#">Home</a>
      <a class="nav-features" href="#">Features</a>
      <a class="nav-clients" href="#">Our Clients</a>
      <a class="nav-company" href="#">Company</a>
      <a class="nav-contact" href="#">Contact</a>
    </nav>
    <a class="cta-button" href="#">Try It Now!</a>
  </header>

  <section class="hero">
    <h1 class="hero-title">Manage Your Workflow Better with Vantel</h1>
    <p class="hero-intro"><strong>The Vantel Assistant</strong> Is A Secure, Sharable Workflow Management Platform Designed With Your Needs In Mind.<br>Here Are Some Features You’ll Love:</p>
    <ul class="feature-list">
      <li class="feature-collab">Built for internal and external collaboration</li>
      <li class="feature-custom">Highly customizable and intuitive</li>
      <li class="feature-free">Free to use – no setup or monthly fees</li>
    </ul>
    <div class="device">
      <div class="device-screen" role="img" aria-label="Screenshot of the Vantel workflow app showing a library list, deal drawers and a working group contact table"></div>
    </div>
  </section>
</body>
</html>
```